Book cover for "The Hollow Ledger"

Cover design measuring 42 x 29 cm + 2 cm trim margin for the non-fiction book "The Hollow Ledger." The content is about business model innovation in the furniture trade. The graphics should reference omnichannel, brick-and-mortar sales, and e-commerce in the furniture trade. The implementation should be playful, perhaps sketchy or abstract. Not conservative! The uploaded file should NOT be a design template. Rather, it should show the content that must be displayed on the cover. The final solution must be delivered in PDF format. The text must be editable.
Look and feel
Each slider illustrates characteristics of the customer's brand and the style your logo design should communicate.

```html
<!DOCTYPE html>
<html lang="en">
<head>
<meta charset="utf-8">
<title>The Hollow Ledger – Book Cover</title>
<link rel="stylesheet" href="https://fonts.googleapis.com/css2?family=Alegreya+Sans:wght@500;700;800&display=swap">
<style>
  :root {
    --stage: #393939;
    --paper: #ffffff;
    --sand: #d4c9b1;
    --ink: #000000;
    --slate-text: #4f6b72;
    --sky-top: #a9c8d6;
    --sky-bottom: #9cbccc;
    --floor: #e6d9c3;
    --wave-blue: #5a9fc0;
    --badge: #6f8f93;
    --white: #ffffff;
  }
  * { margin: 0; padding: 0; box-sizing: border-box; }
  html, body {
    width: 1200px; height: 1200px; overflow: hidden;
    background: var(--stage);
    font-family: "Alegreya Sans", sans-serif;
  }
  .cover {
    position: absolute;
    left: 76px; top: 238px;
    width: 1192px; height: 823px;
    transform: scale(0.8792);
    transform-origin: 0 0;
    background: var(--paper);
    overflow: hidden;
  }
  .front-photo {
    position: absolute;
    left: 624px; top: 0;
    width: 568px; height: 700px;
    background: linear-gradient(180deg, var(--sky-top) 0%, var(--sky-bottom) 78%, #8fb0bd 80%, var(--floor) 82%, #eadfcb 100%);
  }
  .back-swatch {
    position: absolute;
    left: 57px; top: 57px;
    width: 181px; height: 181px;
    background: var(--sand);
  }
  .back-blurb {
    position: absolute;
    left: 57px; top: 322px;
    width: 493px;
    font-size: 22.5px;
    font-weight: 500;
    line-height: 36.6px;
    color: var(--slate-text);
    text-align: justify;
    text-align-last: left;
  }
  .spine-author {
    position: absolute;
    color: var(--ink);
    font-weight: 700;
    white-space: nowrap;
    transform: rotate(-90deg);
    transform-origin: 0 0;
  }
  .spine-author--small { left: 580px; top: 247px; font-size: 20px; }
  .spine-author--large { left: 574px; top: 521px; font-size: 34px; }
  .front-title {
    position: absolute;
    left: 624px; top: 60px;
    width: 500px;
    text-align: center;
    line-height: 1;
  }
  .front-title__kicker {
    display: block;
    font-size: 38px; font-weight: 700;
    color: var(--ink);
    margin-left: 78px;
  }
  .front-title__main {
    display: block;
    font-size: 72px; font-weight: 700;
    color: var(--white);
    margin-top: 2px;
    white-space: nowrap;
  }
  .author-badge {
    position: absolute;
    left: 659px; top: 252px;
    width: 148px; height: 148px;
    border-radius: 50%;
    background: var(--badge);
    color: var(--sand);
    text-align: center;
  }
  .author-badge__small { display: block; font-size: 10px; margin-top: 49px; }
  .author-badge__name { display: block; font-size: 21px; font-weight: 700; margin-top: 6px; }
  .base-wave { position: absolute; left: 0; top: 0; width: 1192px; height: 823px; }
</style>
</head>
<body>
  <main class="cover">
    <div class="front-photo" role="img" aria-label="Photo of a light blue upholstered armchair on a pale wooden floor against a soft blue wall"></div>

    <div class="back-swatch"></div>
    <p class="back-blurb">Duis autem vel eum iriure dolor in hendrerit in vulputate velit esse molestie consequat, vel illum dolore eu feugiat nulla facilisis at vero eros et accumsan et iusto odio dignissim qui blandit praesent luptatum zzril delenit augue duis dolore te feugait nulla facilisi.</p>

    <span class="spine-author spine-author--small">Dorren Vask</span>
    <span class="spine-author spine-author--large">Dorren Vask</span>

    <h1 class="front-title">
      <span class="front-title__kicker">The</span>
      <span class="front-title__main">Hollow Ledger</span>
    </h1>

    <div class="author-badge">
      <span class="author-badge__small">Dorren Vask</span>
      <span class="author-badge__name">Dorren Vask</span>
    </div>

    <svg class="base-wave" viewBox="0 0 1192 823" aria-hidden="true">
      <path fill="var(--wave-blue)" d="M0,823 L0,811 C150,700 330,610 510,610 C640,610 720,655 860,672 C990,682 1100,630 1192,549 L1192,823 Z"/>
      <rect x="199" y="728" width="236" height="35" rx="17.5" fill="var(--sand)"/>
      <rect x="639" y="728" width="237" height="35" rx="17.5" fill="var(--sand)"/>
      <rect x="902" y="728" width="135" height="35" rx="17.5" fill="var(--sand)"/>
    </svg>
  </main>
</body>
</html>
```